Real Estate "For Sale" Sign for construction company

We need a sign that we can use to hang on a post and place on the road when we sell a property. The sign will be simple and will need to mainly feature our logo (files attached), as well as the words "For Sale", and then our phone number "(555) 617 3489". The sign will hang on a post that'll look something like the attached picture.

Target Market(s)

Home buyers

Industry/Entity Type

Real Estate

Font styles to use
Serif
Sans Serif

Colors
0054AA
0677BA
7BADD7
CADEEF
E8F1F8
0094D4
00A9DD
6FCCEA
C7EBF8
E9F6FB

Requirements
Must have
• For Sale & our phone number

```html
<!DOCTYPE html>
<html lang="en">
<head>
<meta charset="utf-8">
<title>For Sale Yard Sign – Cedar Ridge Estates</title>
<link href="https://fonts.googleapis.com/css2?family=Montserrat:wght@500;800&family=Oswald:wght@600&display=swap" rel="stylesheet">
<style>
  :root{
    --backdrop:#eef1f4;
    --sign-white:#ffffff;
    --sky-band:#8fd8f7;
    --mist:#f1f2f3;
    --brand-blue:#0677ba;
    --royal-blue:#0652a8;
    --navy:#141e4a;
    --band-navy:#13205a;
    --band-blue:#0a4fa3;
  }
  *{margin:0;padding:0;box-sizing:border-box}
  html,body{width:1200px;height:1200px;overflow:hidden;background:var(--backdrop)}
  .canvas{position:relative;width:1200px;height:1200px}
  .sign{
    position:absolute;left:175px;top:40px;width:850px;height:1120px;
    background:var(--sign-white);overflow:hidden;
    box-shadow:0 10px 30px rgba(20,30,74,.18);
  }
  .sign__top-band{position:absolute;left:0;top:0;width:100%;height:34px;background:var(--sky-band)}
  .sign__brand{
    position:absolute;left:0;top:150px;width:100%;text-align:center;
    font-family:"Montserrat",sans-serif;font-weight:500;font-size:62px;
    color:var(--brand-blue);letter-spacing:.5px;
  }
  .sign__field{
    position:absolute;left:0;top:322px;width:100%;height:441px;
    background:linear-gradient(180deg,#f7f7f8 0%,var(--mist) 100%);
  }
  .sign__headline{
    position:absolute;left:0;top:355px;width:100%;text-align:center;
    font-family:"Montserrat",sans-serif;font-weight:800;
    font-size:252px;line-height:208px;letter-spacing:2px;
  }
  .sign__headline span{display:block}
  .sign__headline .for{color:var(--royal-blue)}
  .sign__headline .sale{color:var(--navy)}
  .sign__phone-band{
    position:absolute;left:0;top:763px;width:100%;height:134px;
    background:linear-gradient(90deg,var(--band-navy) 0%,var(--band-blue) 50%,var(--band-navy) 100%);
    display:flex;align-items:center;justify-content:center;gap:22px;
  }
  .phone-icon{width:92px;height:92px;flex:none}
  .phone-number{
    font-family:"Oswald",sans-serif;font-weight:600;font-size:104px;
    color:var(--sign-white);letter-spacing:3px;line-height:1;
  }
  .sign__bottom-band{position:absolute;left:0;top:897px;width:100%;height:223px;background:var(--sky-band)}
</style>
</head>
<body>
<div class="canvas">
  <div class="sign">
    <div class="sign__top-band"></div>
    <div class="sign__brand">Cedar Ridge Estates</div>
    <div class="sign__field"></div>
    <h1 class="sign__headline"><span class="for">FOR</span><span class="sale">SALE</span></h1>
    <div class="sign__phone-band">
      <svg class="phone-icon" viewBox="0 0 100 100" aria-hidden="true">
        <circle cx="50" cy="50" r="48" fill="#ffffff"/>
        <path d="M34 26c3-2 6-1 7 2l5 10c1 2 0 5-2 6l-4 3c3 7 8 12 15 15l3-4c1-2 4-3 6-2l10 5c3 1 4 4 2 7l-3 5c-2 3-6 4-10 3-18-5-31-18-36-36-1-4 0-8 3-10z" fill="#13205a"/>
        <path d="M58 30a14 14 0 0 1 12 12" stroke="#13205a" stroke-width="4" fill="none" stroke-linecap="round"/>
        <path d="M58 20a24 24 0 0 1 22 22" stroke="#13205a" stroke-width="4" fill="none" stroke-linecap="round"/>
      </svg>
      <span class="phone-number">(555) 617 3489</span>
    </div>
    <div class="sign__bottom-band"></div>
  </div>
</div>
</body>
</html>
```